flat share room mate rental website(design only)

We need a design for the homepage of a flat share / roommate website. We have a website template http://demo1.lodgeframe.net and we're looking for a homepage similar to this http://uk.bunkpalhub.com but different.
The main user of the site are likely to be students and young professionals so were not looking for anything too serious.
We want to emphasise that the website will be 100% free to use both to post an advert and to contact the advertiser.
We must have a 'new rooms' and new flatmates carousel, also we would prefer if the menu had only a login button and maybe a 'post a room' button.
Our logo is currently being designed, so you can put anything in its place.
We look forward to seeing what you guys come up with.
Target Market(s)
Students, Young Professionals
Industry/Entity Type
Rental
Number of Pages Required
1 page
Look and feel
Each slider illustrates characteristics of the customer's brand and the style your logo design should communicate.

```html
<!DOCTYPE html>
<html lang="en">
<head>
<meta charset="utf-8">
<title>Flatnest – Find Your Perfect Flatmate</title>
<link rel="stylesheet" href="https://fonts.googleapis.com/css2?family=Jockey+One&family=Open+Sans:wght@400;600;700&display=swap">
<style>
:root{
  --orange:#f7a23b;
  --pink:#f08d95;
  --teal:#7cc4b8;
  --teal-btn:#6cbcb1;
  --dark:#1d1d1d;
  --ink:#222;
  --muted:#6b6b6b;
  --light:#f3f3f3;
  --white:#fff;
}
*{box-sizing:border-box;margin:0;padding:0}
html,body{width:1200px;height:3673px;overflow:hidden}
body{font-family:"Open Sans",Arial,sans-serif;color:var(--ink);background:var(--white);position:relative}
.display{font-family:"Jockey One","Arial Narrow",sans-serif;text-transform:uppercase;letter-spacing:2px}

/* header */
.site-header{height:62px;background:var(--dark);display:flex;align-items:center;justify-content:space-between;padding:0 73px}
.brand{color:var(--white);font-family:"Open Sans",Arial,sans-serif;font-weight:600;font-size:16px;display:flex;align-items:center;gap:8px}
.brand-square{width:10px;height:10px;background:var(--orange)}
.main-nav{display:flex;gap:26px;font-size:13px;font-weight:600;text-transform:uppercase}
.main-nav a{color:var(--white);text-decoration:none}
.main-nav a.accent{color:var(--orange)}

/* hero */
.hero{position:relative;height:488px;background:linear-gradient(120deg,#b88f6f 0%,#7d6350 35%,#a7a29b 60%,#d3d0cb 100%)}
.hero-title{position:absolute;top:220px;left:0;right:0;text-align:center;color:var(--white)}
.hero-title .small{font-size:34px;line-height:1}
.hero-title .large{font-size:68px;line-height:1}
.search-bar{position:absolute;top:362px;left:150px;width:900px;height:86px;background:rgba(255,255,255,.55);display:flex;align-items:center;gap:14px;padding:0 22px}
.select{flex:0 0 410px;height:40px;background:var(--white);border:1px solid #ccc;display:flex;align-items:center;justify-content:space-between;padding:0 14px;font-size:13px;color:var(--muted)}
.btn{display:inline-flex;align-items:center;justify-content:center;color:var(--white);font-size:13px;font-weight:600;text-transform:uppercase;text-decoration:none}
.search-bar .btn{flex:1;height:40px}
.btn-orange{background:var(--orange)}
.btn-pink{background:var(--pink)}
.btn-teal{background:var(--teal-btn)}
.fee-band{height:30px;background:var(--teal);color:var(--white);font-size:12px;display:flex;align-items:center;justify-content:center;text-transform:uppercase;letter-spacing:.3px}
.fee-band strong{margin-right:5px}

/* carousels */
.carousel{padding:60px 73px 0;height:446px}
.carousel-head{display:flex;justify-content:space-between;align-items:center;margin-bottom:34px}
.carousel-head h2{font-size:15px;font-weight:700;text-transform:uppercase}
.arrows{display:flex;gap:14px}
.cards{display:grid;grid-template-columns:repeat(4,1fr);gap:25px}
.card{background:var(--white);box-shadow:0 1px 6px rgba(0,0,0,.15);height:293px;position:relative}
.card-photo{height:172px}
.card-body{position:relative;margin-top:-30px;background:var(--white);clip-path:polygon(0 22%,100% 0,100% 100%,0 100%);padding:40px 16px 0;height:151px}
.card-title{font-size:14px;font-weight:700;text-transform:uppercase;border-left:3px solid var(--ink);padding-left:8px;line-height:1}
.card-meta{font-size:11px;color:var(--muted);margin-top:6px}
.card-text{font-size:11px;color:var(--muted);line-height:1.45;margin-top:8px}
.card-foot{display:flex;justify-content:space-between;align-items:center;margin-top:10px}
.card-foot .btn{font-size:9px;padding:5px 12px}
.price{font-size:13px;font-weight:600}

/* stats */
.stats{position:relative;height:500px;background:var(--light);overflow:hidden;text-align:center}
.stats svg.corners{position:absolute;inset:0}
.stats-number{position:relative;color:var(--orange);font-size:56px;padding-top:62px;line-height:1}
.stats-caption{position:relative;font-size:30px;line-height:1.2;margin-top:6px}
.features{position:relative;display:flex;justify-content:center;gap:27px;margin-top:34px}
.feature{width:245px;text-align:left}
.feature-photo{height:177px}
.feature h3{font-size:15px;font-weight:700;text-transform:uppercase;margin-top:18px}
.feature p{font-size:11px;color:var(--muted);line-height:1.5;margin-top:4px}

/* banners */
.banner{position:relative;height:389px;display:flex;align-items:center;justify-content:center;text-align:center;color:var(--white)}
.banner-photo{position:absolute;inset:0;background:linear-gradient(100deg,#3b2a1e,#5a4331 40%,#2c2620 70%,#4a3a2c)}
.banner h2{position:relative;font-size:64px;line-height:1.05}
.cta{position:relative;height:281px;margin-top:30px;text-align:center;color:var(--white)}
.cta .banner-photo{background:linear-gradient(100deg,#2a1f18,#4d3526 45%,#2a2522 75%,#3b2b20)}
.cta-inner{position:relative;padding-top:60px}
.cta .small{font-size:38px;line-height:1}
.cta .large{font-size:64px;line-height:1}
.cta-buttons{display:flex;justify-content:center;gap:14px;margin-top:26px}
.cta-buttons .btn{width:200px;height:36px}

/* press */
.press{height:190px;text-align:center;padding-top:58px}
.press h2{font-size:15px;font-weight:700;text-transform:uppercase}
.press-row{display:flex;justify-content:center;gap:58px;margin-top:30px;color:#b5b5b5;font-size:19px;font-family:Georgia,serif}

/* footer */
.site-footer{height:269px;background:var(--dark);color:var(--white);display:grid;grid-template-columns:repeat(4,1fr);padding:45px 73px 0;gap:20px}
.site-footer h4{font-size:15px;font-weight:600;margin-bottom:12px}
.site-footer li{list-style:none;font-size:11px;color:#cfcfcf;line-height:1.75}
.social{display:flex;gap:6px;margin-top:6px}
.social span{width:22px;height:22px;border-radius:50%;border:1px solid #888}
.bottom-bar{height:93px;background:#efefef;display:flex;align-items:center;padding:0 73px;gap:36px;position:relative}
.bottom-bar .brand{color:var(--ink)}
.legal{font-size:10px;color:var(--muted);line-height:1.6}
.to-top{position:absolute;right:45px;bottom:0;width:64px;height:70px;background:#ddd;display:flex;flex-direction:column;align-items:center;justify-content:center;font-size:11px;font-weight:600;gap:4px}
</style>
</head>
<body>

<header class="site-header">
  <div class="brand"><span class="brand-square"></span>Flatnest</div>
  <nav class="main-nav"><a href="#">Login</a><a href="#" class="accent">Post a Room</a></nav>
</header>

<section class="hero">
  <div role="img" aria-label="Group of smiling young friends relaxing together on a sofa" style="position:absolute;inset:0"></div>
  <div class="hero-title display">
    <div class="small">Find your</div>
    <div class="large">Perfect Flatmate</div>
  </div>
  <form class="search-bar">
    <div class="select">Select Location
      <svg width="10" height="6" viewBox="0 0 10 6"><path d="M0 0l5 6 5-6z" fill="#888"/></svg>
    </div>
    <a class="btn btn-orange" href="#">I need a room</a>
    <a class="btn btn-pink" href="#">I have a room</a>
  </form>
</section>
<div class="fee-band"><strong>No fees:</strong> we don't charge you anything. That means no fees to post an advert and no fees to contact your potential new flatmate</div>

<section class="carousel">
  <div class="carousel-head"><h2>New rooms to rent</h2>
    <div class="arrows">
      <svg width="8" height="12" viewBox="0 0 8 12"><path d="M7 1L2 6l5 5" stroke="#999" stroke-width="2" fill="none"/></svg>
      <svg width="8" height="12" viewBox="0 0 8 12"><path d="M1 1l5 5-5 5" stroke="#333" stroke-width="2" fill="none"/></svg>
    </div>
  </div>
  <div class="cards">
    <article class="card"><div class="card-photo" role="img" aria-label="Bedroom with wooden furniture" style="background:linear-gradient(135deg,#6a3a22,#c8966c)"></div>
      <div class="card-body"><div class="card-title">London</div><p class="card-text">In publishing and graphic reality design, lorem ipsum is a filler visual presentation.</p>
      <div class="card-foot"><a class="btn btn-teal" href="#">Show more</a><span class="price">$250 pcm</span></div></div></article>
    <article class="card"><div class="card-photo" role="img" aria-label="Bright bedroom with double bed" style="background:linear-gradient(135deg,#d8c6b0,#8d6a4e)"></div>
      <div class="card-body"><div class="card-title">London</div><p class="card-text">In publishing and graphic reality design, lorem ipsum is a filler visual presentation.</p>
      <div class="card-foot"><a class="btn btn-teal" href="#">Show more</a><span class="price">$250 pcm</span></div></div></article>
    <article class="card"><div class="card-photo" role="img" aria-label="Modern bedroom with dark headboard" style="background:linear-gradient(135deg,#4a3b33,#b9ab9c)"></div>
      <div class="card-body"><div class="card-title">London</div><p class="card-text">In publishing and graphic reality design, lorem ipsum is a filler visual presentation.</p>
      <div class="card-foot"><a class="btn btn-teal" href="#">Show more</a><span class="price">$250 pcm</span></div></div></article>
    <article class="card"><div class="card-photo" role="img" aria-label="Light bedroom with white linen" style="background:linear-gradient(135deg,#e9e0d4,#a68b6c)"></div>
      <div class="card-body"><div class="card-title">London</div><p class="card-text">In publishing and graphic reality design, lorem ipsum is a filler visual presentation.</p>
      <div class="card-foot"><a class="btn btn-teal" href="#">Show more</a><span class="price">$250 pcm</span></div></div></article>
  </div>
</section>

<section class="stats">
  <svg class="corners" width="1200" height="500" viewBox="0 0 1200 500"><path d="M0 0H130L0 350Z" fill="var(--orange)"/><path d="M1200 40V500H1060Z" fill="var(--orange)"/></svg>
  <div class="stats-number display">8,888,299</div>
  <div class="stats-caption display">Happy flatshares and counting...</div>
  <div class="features">
    <div class="feature"><div class="feature-photo" role="img" aria-label="Spacious bedroom interior" style="background:linear-gradient(135deg,#7a4b2c,#d7b28b)"></div><h3>Great rooms</h3><p>In publishing and graphic design, lorem ipsum is a filler visual presentation.</p></div>
    <div class="feature"><div class="feature-photo" role="img" aria-label="Hand holding a smartphone showing a map" style="background:linear-gradient(135deg,#cfcfcf,#5d6b73)"></div><h3>Easy search</h3><p>In publishing and graphic design, lorem ipsum is a filler visual presentation.</p></div>
    <div class="feature"><div class="feature-photo" role="img" aria-label="Smiling man on the phone" style="background:linear-gradient(135deg,#2f4a66,#9bb3c6)"></div><h3>Expert help 24/7</h3><p>In publishing and graphic design, lorem ipsum is a filler visual presentation.</p></div>
  </div>
</section>

<section class="carousel">
  <div class="carousel-head"><h2>New flatmates</h2>
    <div class="arrows">
      <svg width="8" height="12" viewBox="0 0 8 12"><path d="M7 1L2 6l5 5" stroke="#999" stroke-width="2" fill="none"/></svg>
      <svg width="8" height="12" viewBox="0 0 8 12"><path d="M1 1l5 5-5 5" stroke="#333" stroke-width="2" fill="none"/></svg>
    </div>
  </div>
  <div class="cards">
    <article class="card"><div class="card-photo" role="img" aria-label="Portrait of a young woman" style="background:linear-gradient(135deg,#eaeaea,#7a5a48)"></div>
      <div class="card-body"><div class="card-title">Jelina, 36</div><p class="card-text">In publishing and graphic design, lorem ipsum is a filler visual presentation.</p>
      <div class="card-foot"><a class="btn btn-pink" href="#">Show more</a></div></div></article>
    <article class="card"><div class="card-photo" role="img" aria-label="Portrait of a young man" style="background:linear-gradient(135deg,#8a5a3a,#d2b59a)"></div>
      <div class="card-body"><div class="card-title">John, 38</div><p class="card-text">In publishing and graphic design, lorem ipsum is a filler visual presentation.</p>
      <div class="card-foot"><a class="btn btn-pink" href="#">Show more</a></div></div></article>
    <article class="card"><div class="card-photo" role="img" aria-label="Portrait of a woman with glasses" style="background:linear-gradient(135deg,#d0cfc8,#4f4a44)"></div>
      <div class="card-body"><div class="card-title">Sirlu, 22</div><p class="card-text">In publishing and graphic design, lorem ipsum is a filler visual presentation.</p>
      <div class="card-foot"><a class="btn btn-pink" href="#">Show more</a></div></div></article>
    <article class="card"><div class="card-photo" role="img" aria-label="Portrait of a smiling woman" style="background:linear-gradient(135deg,#f0ece6,#8c5e46)"></div>
      <div class="card-body"><div class="card-title">Serone, 29</div><p class="card-text">In publishing and graphic design, lorem ipsum is a filler visual presentation.</p>
      <div class="card-foot"><a class="btn btn-pink" href="#">Show more</a></div></div></article>
  </div>
</section>

<section class="banner" style="margin-top:10px">
  <div class="banner-photo" role="img" aria-label="Friends lounging together in a shared living room"></div>
  <h2 class="display">Helping you find a flatshare<br>you can call home</h2>
</section>

<section class="carousel" style="height:428px">
  <div class="carousel-head"><h2>Our community</h2>
    <div class="arrows">
      <svg width="8" height="12" viewBox="0 0 8 12"><path d="M7 1L2 6l5 5" stroke="#999" stroke-width="2" fill="none"/></svg>
      <svg width="8" height="12" viewBox="0 0 8 12"><path d="M1 1l5 5-5 5" stroke="#333" stroke-width="2" fill="none"/></svg>
    </div>
  </div>
  <div class="cards">
    <article class="card"><div class="card-photo" role="img" aria-label="Portrait of a bearded man" style="background:linear-gradient(135deg,#e5e5e5,#6b4c3b)"></div>
      <div class="card-body"><div class="card-title">Kelvin</div><div class="card-meta">18-Sep-2014</div><p class="card-text">In publishing and graphic design, lorem ipsum is a filler visual presentation.</p>
      <div class="card-foot"><a class="btn btn-teal" href="#">Show more</a></div></div></article>
    <article class="card"><div class="card-photo" role="img" aria-label="Portrait of a man with glasses" style="background:linear-gradient(135deg,#bfc3c2,#4d3f36)"></div>
      <div class="card-body"><div class="card-title">Joseph</div><div class="card-meta">18-Sep-2014</div><p class="card-text">In publishing and graphic design, lorem ipsum is a filler visual presentation.</p>
      <div class="card-foot"><a class="btn btn-teal" href="#">Show more</a></div></div></article>
    <article class="card"><div class="card-photo" role="img" aria-label="Portrait of a smiling man" style="background:linear-gradient(135deg,#d9b23a,#6d4f2f)"></div>
      <div class="card-body"><div class="card-title">Merrione</div><div class="card-meta">18-Sep-2014</div><p class="card-text">In publishing and graphic design, lorem ipsum is a filler visual presentation.</p>
      <div class="card-foot"><a class="btn btn-teal" href="#">Show more</a></div></div></article>
    <article class="card"><div class="card-photo" role="img" aria-label="Portrait of a man in a blue shirt" style="background:linear-gradient(135deg,#e8e8e8,#5d6f82)"></div>
      <div class="card-body"><div class="card-title">Toms</div><div class="card-meta">18-Sep-2014</div><p class="card-text">In publishing and graphic design, lorem ipsum is a filler visual presentation.</p>
      <div class="card-foot"><a class="btn btn-teal" href="#">Show more</a></div></div></article>
  </div>
</section>

<section class="cta">
  <div class="banner-photo" role="img" aria-label="Group of friends chatting at a table"></div>
  <div class="cta-inner">
    <div class="small display">Find your perfect</div>
    <div class="large display">Flatshare today!</div>
    <div class="cta-buttons"><a class="btn btn-orange" href="#">I need a room</a><a class="btn btn-pink" href="#">I have a room</a></div>
  </div>
</section>

<section class="press">
  <h2>As seen in the press</h2>
  <div class="press-row"><span>The Quillpost</span><span>the fernway</span><span>The Quillpost</span><span>the fernway</span><span>The Quillpost</span><span>the fernway</span></div>
</section>

<footer class="site-footer">
  <div><h4>Popular Cities</h4><ul><li>Lorem Ipsum 1</li><li>Lorem Ipsum 2</li><li>Lorem Ipsum 3</li><li>Lorem Ipsum 4</li><li>Lorem Ipsum 5</li></ul></div>
  <div><h4>Flatshare Types</h4><ul><li>Lorem Ipsum 1</li><li>Lorem Ipsum 2</li><li>Lorem Ipsum 3</li><li>Lorem Ipsum 4</li><li>Lorem Ipsum 5</li></ul></div>
  <div><h4>About Us</h4><ul><li>Need help?</li><li>FAQs</li><li>Press Room</li><li>Website Notes &amp; User Agreements</li><li>Right To Rent</li><li>Become an Affiliate</li><li>Our Pledge</li></ul></div>
  <div><h4>Discover</h4><ul><li>Landlord Zone</li><li>Our Blog</li></ul>
    <h4 style="margin-top:14px">Stay Connected</h4>
    <div class="social"><span></span><span></span><span></span><span></span><span></span><span></span></div></div>
</footer>

<div class="bottom-bar">
  <div class="brand"><span class="brand-square"></span>Flatnest</div>
  <div class="legal">© 2015 Flatnest. All Rights Reserved.<br>Terms &amp; Condition | Privacy Policy</div>
  <div class="to-top"><svg width="12" height="8" viewBox="0 0 12 8"><path d="M1 7l5-5 5 5" stroke="#333" stroke-width="2" fill="none"/></svg>TOP</div>
</div>

</body>
</html>
```